Etiketten-Design für Bier
Zielgruppe
Wie sind eine Brauerei und auch Limonadenhersteller. Zielgruppe sind alle Personen von 16-70.
Aufgabenstellung
In dieser Ausschreibung geht es um eine Etikettengarnitur (Hals- u. Bauchetikett) der Sorte PILS. Die komplette Serie mit Bieretiketten soll jedoch für alle 13 Biersorten neu erstellt werden. Der Gewinner erhält nach Verhandlung/Angebot ebenfalls alle weiteren Sorten. Wir könnten uns vorstellen, für alle Etikettenformate ein ähnliches Schema bzw. Grundgerüst zu verwenden. Sortenspezifisch wird dieses dann an die jeweilige Sorte angepasst. Es sollen nicht alle gleich aussehen und sich nur im Schriftzug unterscheiden. Es wäre zudem schön, wenn die sortentypischen Farben wieder in den neuen Etiketten aufgegriffen werden würden. Unsere Logo und der Slogan 'Leidenschaft Handwerk Qualität' sollte ebenfalls verwendet werden. Alle Stanzen (als Vektorgrafik), Formate, Beispiele, Texte sind im Upload zu finden. Aus Beispielen wie dem HELLES-Etikett können Logo usw. als Vektorgrafik entnommen werden.

```html
<!DOCTYPE html>
<html lang="de">
<head>
<meta charset="utf-8">
<title>Veldt – Etikettenserie</title>
<link rel="stylesheet" href="https://fonts.googleapis.com/css2?family=Roboto+Condensed:wght@300;400;700&display=swap">
<style>
  :root{
    --paper:#e2d8bc;
    --paper-light:#ebe3cb;
    --paper-dark:#d6cbab;
    --ink:#1c1a17;
    --ink-soft:#3a362e;
    --line:#fbf8ef;
    --radler:#f5b80f;
    --pils:#1ca33c;
    --weiss:#1b8fcf;
    --land:#c7202b;
    --bg:#ffffff;
  }
  *{box-sizing:border-box;margin:0;padding:0}
  html,body{width:1200px;height:855px;overflow:hidden;background:var(--bg)}
  body{font-family:"Roboto Condensed",Arial,sans-serif;color:var(--ink)}
  .canvas{position:relative;width:1200px;height:855px}

  .variety{position:absolute;top:0;width:224px;height:855px}
  .variety--radler{left:88px;--accent:var(--radler)}
  .variety--pils{left:350px;--accent:var(--pils)}
  .variety--weiss{left:612px;--accent:var(--weiss)}
  .variety--land{left:883px;--accent:var(--land)}

  /* neck label */
  .neck{position:absolute;top:216px;left:18px;width:188px;height:128px}
  .neck svg{position:absolute;inset:0}
  .neck__paper{fill:var(--paper)}
  .neck__tip{fill:var(--accent)}
  .neck__mark{position:absolute;top:22px;left:50%;transform:translateX(-50%);width:22px;height:22px;border-radius:50%;background:var(--ink-soft)}
  .neck__brand{position:absolute;top:44px;width:100%;text-align:center;font-weight:700;font-size:26px;line-height:1;color:var(--ink)}
  .neck__sort{position:absolute;top:96px;width:100%;text-align:center;font-weight:300;font-size:13px;letter-spacing:.5px;color:var(--accent)}

  /* body label */
  .label{position:absolute;top:464px;left:0;width:224px;height:236px;
    background:linear-gradient(160deg,var(--paper-light),var(--paper) 55%,var(--paper-dark))}
  .label__notch{position:absolute;top:0;left:90px;width:44px;height:20px;background:var(--accent);clip-path:polygon(0 0,100% 0,50% 100%)}
  .label__art{position:absolute;top:24px;left:14px;width:196px;height:108px;border-radius:50%;
    background:radial-gradient(ellipse at center,rgba(251,248,239,.55),rgba(251,248,239,0) 70%)}
  .label__mark{position:absolute;top:44px;left:50%;transform:translateX(-50%);width:40px;height:40px;border-radius:50%;background:var(--ink-soft)}
  .label__since{position:absolute;top:90px;width:100%;text-align:center;font-size:7px;letter-spacing:.6px;color:var(--ink)}
  .label__brand{position:absolute;top:100px;width:100%;text-align:center;font-weight:700;font-size:40px;line-height:1;color:var(--ink)}
  .label__claim{position:absolute;top:144px;width:100%;text-align:center;font-weight:700;font-size:6.5px;letter-spacing:.3px;color:var(--ink)}

  .facts{position:absolute;top:172px;left:34px;width:150px;height:36px;border-top:1px solid var(--ink-soft);
    display:flex;align-items:center}
  .facts__abv{width:34px;font-size:8px;line-height:1.15;color:var(--ink-soft);border-right:1px solid var(--ink-soft);height:24px;padding-top:1px}
  .facts__abv b{display:block;font-weight:400;font-size:10px}
  .facts__sort{flex:1;text-align:center;font-weight:300;font-size:20px;color:var(--accent);letter-spacing:.3px}
  .facts__vol{width:26px;font-size:9px;line-height:1.2;color:var(--ink-soft);border-left:1px solid var(--ink-soft);height:24px;padding-left:4px}

  .label__foot{position:absolute;top:214px;left:34px;width:150px;display:flex;justify-content:space-between;font-size:5.5px;color:var(--ink-soft)}
  .label__band{position:absolute;bottom:0;left:0;width:100%;height:7px;background:var(--accent)}
</style>
</head>
<body>
<main class="canvas">

  <section class="variety variety--radler">
    <div class="neck">
      <svg viewBox="0 0 188 128" width="188" height="128" aria-hidden="true">
        <path class="neck__paper" d="M32 0 L94 26 L156 0 L188 48 L94 128 L0 48 Z"/>
        <path class="neck__tip" d="M75 112 L113 112 L94 128 Z"/>
      </svg>
      <span class="neck__mark"></span>
      <p class="neck__brand">Veldt</p>
      <p class="neck__sort">RADLER</p>
    </div>
    <div class="label">
      <span class="label__notch"></span>
      <div class="label__art" role="img" aria-label="Feine Linienzeichnung eines Fahrrads"></div>
      <span class="label__mark"></span>
      <p class="label__since">SEIT 1937</p>
      <p class="label__brand">Veldt</p>
      <p class="label__claim">LEIDENSCHAFT • HANDWERK • QUALITÄT</p>
      <div class="facts">
        <p class="facts__abv">Alc.Vol.<b>4,8%</b></p>
        <p class="facts__sort">RADLER</p>
        <p class="facts__vol">e<br>0,5l</p>
      </div>
      <div class="label__foot"><span>Mindestens haltbar bis:</span><span>www.brauerei-veldt.de</span></div>
      <span class="label__band"></span>
    </div>
  </section>

  <section class="variety variety--pils">
    <div class="neck">
      <svg viewBox="0 0 188 128" width="188" height="128" aria-hidden="true">
        <path class="neck__paper" d="M32 0 L94 26 L156 0 L188 48 L94 128 L0 48 Z"/>
        <path class="neck__tip" d="M75 112 L113 112 L94 128 Z"/>
      </svg>
      <span class="neck__mark"></span>
      <p class="neck__brand">Veldt</p>
      <p class="neck__sort">PILS</p>
    </div>
    <div class="label">
      <span class="label__notch"></span>
      <div class="label__art" role="img" aria-label="Feine Linienzeichnung von Hopfendolden"></div>
      <span class="label__mark"></span>
      <p class="label__since">SEIT 1937</p>
      <p class="label__brand">Veldt</p>
      <p class="label__claim">LEIDENSCHAFT • HANDWERK • QUALITÄT</p>
      <div class="facts">
        <p class="facts__abv">Alc.Vol.<b>4,8%</b></p>
        <p class="facts__sort">PILS</p>
        <p class="facts__vol">e<br>0,5l</p>
      </div>
      <div class="label__foot"><span>Mindestens haltbar bis:</span><span>www.brauerei-veldt.de</span></div>
      <span class="label__band"></span>
    </div>
  </section>

  <section class="variety variety--weiss">
    <div class="neck">
      <svg viewBox="0 0 188 128" width="188" height="128" aria-hidden="true">
        <path class="neck__paper" d="M32 0 L94 26 L156 0 L188 48 L94 128 L0 48 Z"/>
        <path class="neck__tip" d="M75 112 L113 112 L94 128 Z"/>
      </svg>
      <span class="neck__mark"></span>
      <p class="neck__brand">Veldt</p>
      <p class="neck__sort">WEIßBIER</p>
    </div>
    <div class="label">
      <span class="label__notch"></span>
      <div class="label__art" role="img" aria-label="Feine Linienzeichnung einer Brezel"></div>
      <span class="label__mark"></span>
      <p class="label__since">SEIT 1937</p>
      <p class="label__brand">Veldt</p>
      <p class="label__claim">LEIDENSCHAFT • HANDWERK • QUALITÄT</p>
      <div class="facts">
        <p class="facts__abv">Alc.Vol.<b>4,8%</b></p>
        <p class="facts__sort">WEIßBIER</p>
        <p class="facts__vol">e<br>0,5l</p>
      </div>
      <div class="label__foot"><span>Mindestens haltbar bis:</span><span>www.brauerei-veldt.de</span></div>
      <span class="label__band"></span>
    </div>
  </section>

  <section class="variety variety--land">
    <div class="neck">
      <svg viewBox="0 0 188 128" width="188" height="128" aria-hidden="true">
        <path class="neck__paper" d="M32 0 L94 26 L156 0 L188 48 L94 128 L0 48 Z"/>
        <path class="neck__tip" d="M75 112 L113 112 L94 128 Z"/>
      </svg>
      <span class="neck__mark"></span>
      <p class="neck__brand">Veldt</p>
      <p class="neck__sort">LANDBIER</p>
    </div>
    <div class="label">
      <span class="label__notch"></span>
      <div class="label__art" role="img" aria-label="Feine Linienzeichnung eines Brotlaibs mit Ähre"></div>
      <span class="label__mark"></span>
      <p class="label__since">SEIT 1937</p>
      <p class="label__brand">Veldt</p>
      <p class="label__claim">LEIDENSCHAFT • HANDWERK • QUALITÄT</p>
      <div class="facts">
        <p class="facts__abv">Alc.Vol.<b>4,8%</b></p>
        <p class="facts__sort">LANDBIER</p>
        <p class="facts__vol">e<br>0,5l</p>
      </div>
      <div class="label__foot"><span>Mindestens haltbar bis:</span><span>www.brauerei-veldt.de</span></div>
      <span class="label__band"></span>
    </div>
  </section>

</main>
</body>
</html>
```